K&R Security Services PTY. LTD.

Ive just had my logo made and I'm looking for some simple but strong designs for my business cards the company is a security company.

Please use dark colors.

Regards,

Owen Deloit

Reason: Need more time for discussion with other directors

Industry/Entity Type

Security

Font styles to use
Sans Serif
Decorative

```html
<!DOCTYPE html>
<html lang="en">
<head>
<meta charset="utf-8">
<title>K&amp;R Security Services – Business Cards</title>
<link rel="stylesheet" href="https://fonts.googleapis.com/css2?family=Michroma&family=Questrial&display=swap">
<style>
  :root {
    --backdrop: #5e5e5e;
    --card-dark: #2b2b2b;
    --card-light: #ffffff;
    --ink-dark: #2b2b2b;
    --ink-light: #f2f2f2;
    --ink-muted: #c9c9c9;
  }
  * { box-sizing: border-box; margin: 0; padding: 0; }
  html, body {
    width: 1200px; height: 1000px; overflow: hidden;
    background: var(--backdrop);
  }
  .sheet {
    position: relative; width: 1200px; height: 1000px;
    display: flex; flex-direction: column; align-items: center; justify-content: center; gap: 60px;
  }
  .card {
    position: relative; width: 700px; height: 400px;
    box-shadow: 0 6px 18px rgba(0,0,0,.35);
    overflow: hidden;
    font-family: "Questrial", sans-serif;
  }
  /* Front */
  .card--front { display: flex; background: var(--card-dark); }
  .front__brand {
    width: 284px; background: var(--card-light);
    display: flex; align-items: center; justify-content: center;
  }
  .brand-mark {
    display: flex; align-items: center; gap: 10px;
    color: var(--ink-dark); font-family: "Questrial", sans-serif;
    font-size: 19px; line-height: 1.25;
  }
  .brand-mark__square { width: 14px; height: 14px; background: var(--ink-dark); flex: none; }
  .front__details {
    flex: 1; position: relative; padding: 44px 0 0 46px; color: var(--ink-light);
  }
  .holder__name {
    font-family: "Michroma", sans-serif; font-size: 28px; letter-spacing: 0.5px; font-weight: 400;
  }
  .holder__role { margin-top: 6px; font-size: 16px; color: var(--ink-muted); }
  .contact {
    position: absolute; left: 46px; bottom: 46px; list-style: none;
    font-size: 18px; line-height: 22px;
  }
  .contact li { display: flex; align-items: center; gap: 8px; }
  .contact svg { width: 13px; height: 13px; fill: var(--ink-muted); }
  /* Back */
  .card--back { background: var(--card-light); }
  .back__brand {
    position: absolute; inset: 0 0 68px 0;
    display: flex; align-items: center; justify-content: center;
  }
  .back__brand .brand-mark { font-size: 26px; }
  .back__brand .brand-mark__square { width: 18px; height: 18px; }
  .back__band {
    position: absolute; left: 0; right: 0; bottom: 0; height: 68px;
    background: var(--card-dark); color: var(--ink-light);
    display: flex; align-items: center; justify-content: center;
    font-size: 20px; letter-spacing: .5px;
  }
</style>
</head>
<body>
<main class="sheet">
  <section class="card card--front">
    <div class="front__brand">
      <div class="brand-mark"><span class="brand-mark__square"></span><span>K&amp;R Security<br>Services</span></div>
    </div>
    <div class="front__details">
      <h1 class="holder__name">Owen Deloit</h1>
      <p class="holder__role">Owner</p>
      <ul class="contact">
        <li><svg viewBox="0 0 12 12"><rect x="3" y="0" width="6" height="12" rx="1.2"/></svg>+00 412 555 018</li>
        <li><svg viewBox="0 0 12 12"><path d="M2 1l3 0 1 3-2 1c1 2 2 3 4 4l1-2 3 1 0 3c-6 0-10-4-10-10z"/></svg>+00 3 5550 2741</li>
        <li><svg viewBox="0 0 12 12"><path d="M0 3h12v8H0z M0 3l6 4 6-4"/></svg>owen@krsecure.net</li>
      </ul>
    </div>
  </section>

  <section class="card card--back">
    <div class="back__brand">
      <div class="brand-mark"><span class="brand-mark__square"></span><span>K&amp;R Security Services</span></div>
    </div>
    <div class="back__band">www.krsecure.net</div>
  </section>
</main>
</body>
</html>
```